Buchcover-Design für Erziehungsratgeber
Zielgruppe
Es handelt sich um einen Erziehungsratgeber zum Thema 'bedürfnisorientierte Erziehung'.
Zielgruppe :
Frauen 25-35 Jahre
Werdende Mütter bzw. Mütter eines Neugeborenen
Personen mit Vorliebe für natürliche Heilmittel, Methoden oder Konzepte.
Personen, die eher Vorbehalte ggü. chemischen, kommerziellen oder industriellen Heilmitteln, Methoden, Konzepten haben.
Aufgabenstellung
Das Cover soll ein Baby 1-12 Monate zeigen, ggf. auch mit der Mutter zusammen.
Das Cover soll Schutz, Geborgenheit und Fürsorge ausstrahlen.
Eine kreativere Titel-Anordnung ist gewünscht. Bitte wählen Sie für die Titel-Anordnung KEINE Standard-Anordnung, also z.B. nicht mittig zentriert im oberen Drittel.
Farbvorschlag für den Titel-Text: 800080ff (abweichende Ideen sind trotzdem gern gesehen)
Stockmaterial wird von Bildtruhenarchiv.com bevorzugt.
Cover-Maße: 6x9 Zoll, 170 Seiten. Bitte Template benutzen.
Das Verlagslogo soll unten Links auf dem Cover abgedruckt werden. Bitte wählen Sie eine zum Cover passende, unauffällige Farbe.
Titel: 'Achtsames Aufwachsen mit Nähe und Vertrauen im ersten Lebensjahr'
Sub-Titel (unauffällig darstellen): 'So begleiten Sie Ihren Säugling mit Ruhe und Feingefühl durch die ersten Wochen und erkennen, welche Signale er Ihnen sendet. Ein Familienbegleiter für das erste Jahr mit Kind'
Autoren-Name: 'Helga Brink'

```html
<!DOCTYPE html>
<html lang="de">
<head>
<meta charset="utf-8">
<title>Achtsames Aufwachsen – Buchumschlag</title>
<link rel="stylesheet" href="https://fonts.googleapis.com/css2?family=Roboto:wght@300;400;500&family=Roboto+Condensed:wght@300;400&display=swap">
<style>
  :root {
    --plum: #800080;
    --plum-soft: #86118a;
    --white: #ffffff;
    --window: #f6f5f6;
    --sheet: #ecebee;
    --sheet-shade: #dcdade;
    --shirt: #e8837a;
    --skin: #efc9b8;
    --pillow: #8fb8bd;
    --headboard: #e6d6c9;
  }
  * { margin: 0; padding: 0; box-sizing: border-box; }
  html, body { width: 1200px; height: 874px; overflow: hidden; background: var(--white); }
  .cover-wrap { position: relative; width: 1200px; height: 874px; }

  .back-cover {
    position: absolute; left: 0; top: 0; width: 616px; height: 874px;
    background: linear-gradient(180deg, var(--plum-soft) 0%, var(--plum) 100%);
    color: var(--white);
    font-family: 'Roboto', sans-serif;
  }
  .back-heading {
    position: absolute; left: 50px; top: 100px; width: 490px;
    text-align: center; font-weight: 500; font-size: 21px;
    line-height: 33px; letter-spacing: 1.2px; text-transform: uppercase;
  }
  .back-blurb {
    position: absolute; left: 67px; top: 180px; width: 454px;
    font-size: 14.3px; line-height: 23.7px; letter-spacing: 0.5px; font-weight: 400;
  }
  .barcode-area {
    position: absolute; left: 366px; top: 727px; width: 191px; height: 116px;
    background: var(--white);
  }

  .spine-title, .spine-author {
    position: absolute; left: 597px; color: var(--white);
    font-family: 'Roboto', sans-serif; font-weight: 500; text-transform: uppercase;
    white-space: nowrap; transform-origin: 0 0;
    transform: rotate(-90deg) translate(-100%, -50%);
  }
  .spine-title { top: 39px; font-size: 13.4px; letter-spacing: 0.9px; width: 585px; text-align: right; }
  .spine-author { top: 720px; font-size: 15px; letter-spacing: 1px; width: 107px; text-align: right; }

  .front-cover {
    position: absolute; left: 616px; top: 0; width: 584px; height: 874px;
    overflow: hidden;
  }
  .front-photo {
    position: absolute; inset: 0;
    background:
      radial-gradient(ellipse 22% 38% at 92% 38%, var(--shirt) 0%, rgba(232,131,122,0.6) 55%, rgba(232,131,122,0) 100%),
      radial-gradient(ellipse 38% 14% at 62% 78%, var(--skin) 0%, rgba(239,201,184,0.5) 60%, rgba(239,201,184,0) 100%),
      radial-gradient(ellipse 16% 5% at 57% 56%, var(--pillow) 0%, rgba(143,184,189,0) 100%),
      radial-gradient(ellipse 30% 8% at 72% 50%, var(--headboard) 0%, rgba(230,214,201,0) 100%),
      linear-gradient(180deg, var(--window) 0%, var(--window) 50%, var(--sheet) 62%, var(--sheet-shade) 100%);
  }
  .front-author {
    position: absolute; left: 203px; top: 31px;
    font-family: 'Roboto', sans-serif; font-weight: 300; font-size: 24px;
    letter-spacing: 2px; color: var(--plum);
  }
  .front-title {
    position: absolute; left: 33px; top: 108px; color: var(--plum);
    font-family: 'Roboto Condensed', sans-serif; font-weight: 400;
  }
  .front-title span { display: block; white-space: nowrap; }
  .title-line-one { font-size: 42px; line-height: 48px; letter-spacing: 0.5px; }
  .title-line-big { font-size: 86px; line-height: 80px; letter-spacing: 0.5px; }
  .title-line-big small { font-size: 28px; letter-spacing: 0.5px; margin-left: 6px; }
  .title-line-three, .title-line-four { font-size: 48px; line-height: 50px; letter-spacing: 1px; }

  .front-subtitle {
    position: absolute; left: 35px; top: 372px; width: 300px;
    font-family: 'Roboto Condensed', sans-serif; font-weight: 300;
    font-size: 14px; line-height: 20px; color: var(--plum);
  }

  .publisher {
    position: absolute; left: 39px; top: 810px; color: var(--plum);
    font-family: 'Roboto', sans-serif; font-weight: 500; font-size: 19px;
    letter-spacing: 1px;
  }
</style>
</head>
<body>
<div class="cover-wrap">
  <section class="back-cover">
    <h2 class="back-heading">Achtsames Aufwachsen mit Nähe und Vertrauen im ersten Lebensjahr</h2>
    <p class="back-blurb">Lorem ipsum dolor sit amet, consectetuer adipiscing elit. Aenean commodo ligula eget dolor. Aenean massa. Cum sociis natoque penatibus et magnis dis parturient montes, nascetur ridiculus mus. Donec quam felis, ultricies nec, pellentesque eu, pretium quis, sem. Nulla consequat massa quis enim. Donec pede justo, fringilla vel, aliquet nec, vulputate eget, arcu. In enim justo, rhoncus ut, imperdiet a, venenatis vitae, justo. Nullam dictum felis eu pede mollis pretium. Integer tincidunt. Cras dapibus. Vivamus elementum semper nisi. Aenean vulputate eleifend tellus. Aenean leo ligula, porttitor eu, consequat vitae, eleifend ac, enim. Aliquam lorem ante, dapibus in, viverra quis, feugiat a, tellus.</p>
    <div class="barcode-area"></div>
    <div class="spine-title">Achtsames Aufwachsen mit Nähe und Vertrauen im ersten Lebensjahr</div>
    <div class="spine-author">Helga Brink</div>
  </section>

  <section class="front-cover">
    <div class="front-photo" role="img" aria-label="Foto: Mutter in korallfarbenem Shirt hält die Füße ihres Babys, das auf einem weißen Bett liegt, vor hellem Fenster mit Kissen und Kopfteil"></div>
    <div class="front-author">HELGA BRINK</div>
    <h1 class="front-title">
      <span class="title-line-one">Achtsames Aufwachsen</span>
      <span class="title-line-big">mit Nähe<small>und</small></span>
      <span class="title-line-three">Vertrauen im ersten</span>
      <span class="title-line-four">Lebensjahr</span>
    </h1>
    <p class="front-subtitle">So begleiten Sie Ihren Säugling mit Ruhe und Feingefühl durch die ersten Wochen und erkennen, welche Signale er Ihnen sendet. Ein Familienbegleiter für das erste Jahr mit Kind</p>
    <div class="publisher">Falke Verlag</div>
  </section>
</div>
</body>
</html>
```